Financial Consulting Company in need of technical diagram

Attached is a basic template to follow, however the following changes must be made:
- Get rid of reflection boxes at the bottom
-Delete anything in parentheses
-Change top box to read "Uncover Value Opportunities"
-Change bottom right box to read "Sales and Operations Planning"
-Change bottom left box to read "Financial Planning"

Additionally we would like to see something a little more creative and cohesive. One possibility is using "Cheveron" type arrows to show the "wheel" effect.

Please email tmorven@brightlake7.example if you have any questions!
Updates

Please see newly uploaded image for an example of how we would like it re-created.

Industry/Entity Type

Financial

Requirements
Must have
• I'm looking for something that keeps the "wheel" approach, but is not a direct re-creation of the example given. The boxes for example, dont' necessarily need to stay boxes. Feel free to play around with placement as well.
Nice to have
• Please see green wheel for example of how it can be re-created.

```html
<!DOCTYPE html>
<html lang="en">
<head>
<meta charset="utf-8">
<title>Value Cycle Diagram</title>
<link href="https://fonts.googleapis.com/css2?family=Open+Sans:wght@700&display=swap" rel="stylesheet">
<style>
  :root {
    --bg: #ffffff;
    --node-light: #a572c4;
    --node-mid: #7a3a9e;
    --node-dark: #4a1968;
    --node-text: #ffffff;
    --arrow-light: #d2f08a;
    --arrow-mid: #8fd14a;
    --arrow-dark: #3f9a2a;
  }
  html, body {
    margin: 0;
    padding: 0;
    width: 1200px;
    height: 1159px;
    overflow: hidden;
    background: var(--bg);
  }
  .cycle {
    position: relative;
    width: 1200px;
    height: 1159px;
  }
  .cycle__arrows {
    position: absolute;
    inset: 0;
  }
  .stage {
    position: absolute;
    width: 266px;
    height: 266px;
    margin: -133px 0 0 -133px;
    border-radius: 50%;
    background:
      radial-gradient(circle at 38% 28%, var(--node-light) 0%, var(--node-mid) 45%, var(--node-dark) 100%);
    box-shadow: inset 0 -10px 24px rgba(40, 8, 60, 0.45), 0 4px 10px rgba(60, 20, 80, 0.25);
    display: flex;
    align-items: center;
    justify-content: center;
    text-align: center;
  }
  .stage__label {
    font-family: "Open Sans", Verdana, sans-serif;
    font-weight: 700;
    font-size: 32px;
    line-height: 1.12;
    color: var(--node-text);
    text-shadow: 0 2px 3px rgba(30, 0, 50, 0.55);
  }
  .stage--uncover   { left: 600px;  top: 144px; }
  .stage--strategize{ left: 1029px; top: 465px; }
  .stage--sop       { left: 877px;  top: 968px; }
  .stage--financial { left: 332px;  top: 973px; }
  .stage--assess    { left: 160px;  top: 465px; }
</style>
</head>
<body>
<main class="cycle">
  <svg class="cycle__arrows" width="1200" height="1159" viewBox="0 0 1200 1159" aria-hidden="true">
    <defs>
      <linearGradient id="arrow-fill" x1="0" y1="0" x2="1" y2="1">
        <stop offset="0" stop-color="var(--arrow-light)"/>
        <stop offset="0.5" stop-color="var(--arrow-mid)"/>
        <stop offset="1" stop-color="var(--arrow-dark)"/>
      </linearGradient>
      <path id="cycle-arrow" d="M1067,603 A467,467 0 0 1 1033,778 L1063.6,790.3 L968.9,851.8 L961.6,749.1 L992.2,761.5 A423,423 0 0 0 1023,603 Z" fill="url(#arrow-fill)"/>
    </defs>
    <use href="#cycle-arrow" transform="rotate(-71 600 603)"/>
    <use href="#cycle-arrow" transform="rotate(1 600 603)"/>
    <use href="#cycle-arrow" transform="rotate(72 600 603)"/>
    <use href="#cycle-arrow" transform="rotate(145 600 603)"/>
    <use href="#cycle-arrow" transform="rotate(216 600 603)"/>
  </svg>

  <div class="stage stage--uncover"><span class="stage__label">Uncover<br>Value<br>Opportunities</span></div>
  <div class="stage stage--strategize"><span class="stage__label">Strategize<br>and<br>Align</span></div>
  <div class="stage stage--sop"><span class="stage__label">Sales and<br>Operations<br>Planning</span></div>
  <div class="stage stage--financial"><span class="stage__label">Financial<br>Planning</span></div>
  <div class="stage stage--assess"><span class="stage__label">Assess<br>the<br>Results</span></div>
</main>
</body>
</html>
```